IT Network Consultancy - Business Card

t4 linkways is a IT network consultancy based in London. We're looking for a smart, modern and professional business card design. Our website is here: www.t4linkways.co.uk

Key things that should be included on the card (with examples):

Company Logo
Name
Position / Job Title: Network Consultant
Mobile Phone Number: +44 (0) 7700 900418
Land Line: +44 (0) 1632 960274
Email Address: name@t4linkways.co.uk
Web Site URL: www.t4linkways.co.uk

Target Market(s)

Large enterprise / global companies / corporates

Industry/Entity Type

Business

Requirements
Must have
• Incorporate our logo - which is attached to the project. They are in AI format (can be opened in Inkscape).

The design should be double sided and fit on a UK standard 85mm × 55mm card and be in a format that retains the quality when printed.
Nice to have
• The project does not have to conform to the colour of our website but this should give you inspiration of the style we like.
Should not have
• Bright colours. Pictures are not necessary.

```html
<!DOCTYPE html>
<html lang="en">
<head>
<meta charset="utf-8">
<title>t4 linkways – Business Card</title>
<link rel="stylesheet" href="https://fonts.googleapis.com/css2?family=Exo+2:wght@300;400&display=swap">
<style>
  :root {
    --navy-deep: #06204f;
    --navy-mid: #0f2d70;
    --navy-bright: #1a3d96;
    --steel: #8f9ca8;
    --silver: #c8ccd4;
    --white: #ffffff;
    --stripe-blue: #1c3f9c;
  }
  * { margin: 0; padding: 0; box-sizing: border-box; }
  html, body {
    width: 1200px;
    height: 777px;
    overflow: hidden;
    background: var(--navy-deep);
  }
  .card {
    position: relative;
    width: 1200px;
    height: 777px;
    overflow: hidden;
    background: linear-gradient(215deg, var(--navy-bright) 0%, var(--navy-mid) 45%, var(--navy-deep) 100%);
    font-family: "Exo 2", sans-serif;
  }
  .hardware-band {
    position: absolute;
    inset: 0;
    width: 1200px;
    height: 777px;
  }
  .brand-logo {
    position: absolute;
    left: 448px;
    top: 36px;
    transform: translateX(-50%);
    color: var(--steel);
    font-weight: 400;
    font-size: 190px;
    line-height: 0.95;
    letter-spacing: 2px;
    text-align: center;
    white-space: nowrap;
  }
  .brand-logo span { display: block; }
  .person-name {
    position: absolute;
    left: 226px;
    top: 528px;
    color: var(--steel);
    font-weight: 400;
    font-size: 72px;
    line-height: 1;
    font-variant: small-caps;
    letter-spacing: 5px;
    white-space: nowrap;
  }
  .job-title {
    position: absolute;
    left: 162px;
    top: 672px;
    color: var(--white);
    font-weight: 400;
    font-size: 54px;
    line-height: 1;
    font-variant: small-caps;
    letter-spacing: 6px;
    white-space: nowrap;
  }
  .contact-list {
    position: absolute;
    right: 40px;
    top: 36px;
    list-style: none;
    color: var(--white);
    font-weight: 300;
    font-size: 24px;
    line-height: 1.45;
    letter-spacing: 1px;
    text-align: right;
    white-space: nowrap;
  }
</style>
</head>
<body>
  <main class="card">
    <svg class="hardware-band" viewBox="0 0 1200 777" xmlns="http://www.w3.org/2000/svg">
      <polygon role="img" aria-label="Illustration of network hardware panel with a globe"
               points="1200,185 1200,777 765,777" fill="var(--silver)"/>
      <polygon points="1200,276 1200,286 841,777 829,777" fill="var(--stripe-blue)"/>
    </svg>

    <h1 class="brand-logo"><span>t4</span><span>linkways</span></h1>

    <ul class="contact-list">
      <li>M: +44 (0) 7700 900418</li>
      <li>T: +44 (0) 1632 960274</li>
      <li>name@t4linkways.co.uk</li>
      <li>www.t4linkways.co.uk</li>
    </ul>

    <p class="person-name">Alex Morgan</p>
    <p class="job-title">Network Consultant</p>
  </main>
</body>
</html>
```